Kestwick Holdings AG needs web design

We need a website for a Swiss company: Kestwick Holdings AG. We offer our customers financial services such as advice and funds. We also have an interest rate calculator that we want to link to via a button on the website.

We are looking for a black and gold design. (Background: Black, Accents: Gold and White)
The design should convey security and growth. We have uploaded our logo in the attachment.
Font from the logo: Trajan Pro Regular

```html
<!DOCTYPE html>
<html lang="en">
<head>
<meta charset="utf-8">
<title>Kestwick Holdings AG</title>
<link rel="stylesheet" href="https://fonts.googleapis.com/css2?family=Cinzel:wght@400;600&family=Mulish:wght@400;600&display=swap">
<style>
:root{
  --black:#000;
  --panel:#0b0b0b;
  --card:#131313;
  --field:#141414;
  --gold:#b08b4a;
  --gold-light:#e3c882;
  --gold-dark:#8a6a32;
  --white:#fff;
  --text:#d9d9d9;
  --muted:#9a9a9a;
}
*{box-sizing:border-box;margin:0;padding:0}
html,body{width:1200px;height:4295px;overflow:hidden;background:var(--black)}
body{font-family:'Mulish',sans-serif;color:var(--text);font-size:15px;line-height:1.75}
section,header,footer{position:relative;width:1200px;overflow:hidden}
.btn-gold{display:inline-block;border-radius:30px;background:linear-gradient(90deg,var(--gold-dark),var(--gold-light) 60%,var(--gold));color:var(--white);font-family:'Cinzel',serif;font-weight:600;text-align:center;text-decoration:none}
.eyebrow{font-family:'Cinzel',serif;color:var(--gold);font-size:16px;text-align:center}
.section-title{font-family:'Cinzel',serif;color:var(--white);font-size:38px;font-weight:400;text-align:center;line-height:1.2;letter-spacing:1px}

/* nav */
.site-nav{height:80px;background:var(--black);z-index:3;overflow:visible}
.site-nav a{position:absolute;top:26px;color:var(--white);font-size:15px;text-decoration:none}
.site-nav a.active{color:var(--gold)}
.nav-mark{position:absolute;left:535px;top:0;width:130px;height:105px;border-radius:0 0 65px 65px;background:#0d0d0d;display:flex;align-items:center;justify-content:center;text-align:center;font-family:'Cinzel',serif;color:var(--gold);font-size:12px;line-height:1.2;padding-bottom:14px}
.site-nav .btn-gold{top:18px;left:937px;width:144px;height:38px;line-height:38px;font-size:16px}

/* hero */
.hero{height:687px}
.hero-art{position:absolute;left:0;top:0;width:1200px;height:687px;
  background:
    radial-gradient(ellipse 55% 18% at 55% 86%,rgba(176,139,74,.35) 0%,rgba(176,139,74,0) 100%),
    radial-gradient(ellipse at 60% 32%,#4a3a1e 0%,#241b0d 35%,#0a0805 62%,#000 80%)}
.hero-name{position:absolute;top:200px;width:1200px;text-align:center;font-family:'Cinzel',serif;color:var(--gold-light);font-size:38px;line-height:1.2;letter-spacing:2px}
.hero-name small{display:block;font-size:30px}
.hero-title{position:absolute;top:322px;width:1200px;text-align:center;font-family:'Cinzel',serif;font-weight:400;color:var(--white);font-size:42px;line-height:52px;letter-spacing:2px}

/* about */
.about{height:470px}
.about-mark{position:absolute;left:118px;top:80px;width:430px;height:290px;display:flex;align-items:center;justify-content:center;font-family:'Cinzel',serif;color:var(--gold);font-size:62px;line-height:1.1;text-align:center}
.about-body{position:absolute;left:630px;top:70px;width:450px}
.about-body .eyebrow{text-align:left;font-size:15px}
.about-body h2{font-family:'Cinzel',serif;color:var(--white);font-size:37px;font-weight:400;line-height:1.2;margin:2px 0 10px}
.about-body p{font-size:14.5px;line-height:26px}
.about-body .btn-gold{margin-top:28px;width:172px;height:52px;line-height:52px;font-size:17px}

/* services */
.services{height:625px;background:var(--panel)}
.services .eyebrow{padding-top:65px}
.service-list{position:absolute;top:188px;left:112px;display:flex;gap:25px}
.service-card{width:310px;height:328px;background:var(--card);text-align:center;padding:32px 22px 0}
.service-card svg{display:block;margin:0 auto}
.service-card h3{font-family:'Cinzel',serif;color:var(--gold);font-weight:400;font-size:21px;margin:16px 0 8px}
.service-card p{font-size:14.5px;line-height:26px}
.circle-btn{display:block;width:47px;height:47px;margin:28px auto 0;border-radius:50%;background:var(--gold);position:relative}
.circle-btn::after{content:"";position:absolute;left:17px;top:18px;width:8px;height:8px;border-top:2px solid var(--white);border-right:2px solid var(--white);transform:rotate(45deg)}

/* testimonials */
.testimonials{height:593px}
.testimonials .eyebrow{padding-top:80px;font-size:15px}
.review-list{position:absolute;top:183px;left:180px;display:flex;gap:39px}
.review{width:408px;height:322px;background:var(--card);padding:28px 26px}
.review h3{font-family:'Cinzel',serif;color:var(--white);font-weight:400;font-size:27px;line-height:38px;margin:8px 0 12px}
.review p{font-size:14.5px;line-height:26px}
.reviewer{display:flex;align-items:center;gap:12px;margin-top:10px}
.avatar{width:45px;height:45px;border-radius:50%;background:radial-gradient(circle,#8a7a66,#3b3128)}
.reviewer b{display:block;font-family:'Cinzel',serif;color:var(--white);font-weight:600;font-size:16px;line-height:20px}
.reviewer span{font-size:14.5px;line-height:20px}

/* blog */
.blog{height:712px;background:var(--panel)}
.blog .eyebrow{padding-top:65px}
.post-grid{position:absolute;top:180px;left:112px;display:grid;grid-template-columns:475px 475px;gap:32px 26px}
.post{height:208px;background:var(--card);display:flex;border-radius:6px;overflow:hidden}
.post-photo{width:223px;height:208px;flex:none}
.post-body{padding:18px 24px}
.post-body h3{font-family:'Cinzel',serif;color:var(--white);font-weight:400;font-size:25px;line-height:1.2}
.post-body time{display:block;color:var(--gold);font-size:14.5px;margin:2px 0 6px}
.post-body p{font-size:14.5px;line-height:26px}
.post-body a{font-family:'Cinzel',serif;color:var(--gold);font-size:15px;text-decoration:none}

/* contact */
.contact{height:516px}
.contact h2{position:absolute;left:158px;top:92px;font-family:'Cinzel',serif;font-weight:400;color:var(--white);font-size:40px;line-height:1.2}
.contact-list{position:absolute;left:158px;top:175px;width:330px;list-style:none}
.contact-list li{position:relative;padding-left:30px;margin-bottom:28px;font-size:14.5px;line-height:22px}
.contact-list svg{position:absolute;left:2px;top:3px}
.contact-list b{display:block;font-family:'Cinzel',serif;color:var(--white);font-size:17px;font-weight:600}
.contact-form{position:absolute;left:548px;top:100px;width:490px}
.field{height:57px;background:var(--field);margin-bottom:17px;padding:16px 28px;color:var(--white);font-size:15px}
.contact-form .btn-gold{margin:17px 0 0 5px;width:154px;height:50px;line-height:50px;font-size:17px}

/* footer */
.site-footer{height:612px;background:linear-gradient(180deg,#000 0%,#0b0a08 45%,#0d0c0a 100%)}
.footer-art{position:absolute;left:0;top:60px;width:1200px;height:260px;
  background:
    radial-gradient(ellipse 45% 40% at 55% 35%,rgba(176,139,74,.22) 0%,rgba(176,139,74,0) 100%),
    radial-gradient(ellipse 14% 45% at 12% 70%,rgba(176,139,74,.2) 0%,rgba(176,139,74,0) 100%)}
.footer-name{position:absolute;left:112px;top:310px;width:270px;text-align:center;font-family:'Cinzel',serif;color:var(--gold);font-size:30px;line-height:1.2}
.footer-col{position:absolute;top:250px}
.footer-col h4{font-family:'Cinzel',serif;color:var(--gold);font-weight:400;font-size:24px;line-height:1.3;margin-bottom:10px}
.footer-col ul{list-style:none}
.footer-col li{color:var(--white);font-size:14.5px;line-height:30px;display:flex;align-items:center;gap:9px}
.chev{width:6px;height:6px;border-top:1.5px solid var(--white);border-right:1.5px solid var(--white);transform:rotate(45deg)}
.dot{width:10px;height:10px;border-radius:50%;background:var(--white)}
.news-field{width:242px;border-bottom:1px solid #555;color:var(--muted);font-size:14px;padding:2px 0 6px;margin-bottom:18px}
.footer-col .btn-gold{width:152px;height:40px;line-height:40px;font-size:16px;margin-top:14px}
.copyright{position:absolute;top:545px;width:1200px;text-align:center;color:var(--white);font-size:14.5px}
</style>
</head>
<body>

<header class="site-nav">
  <a href="#" class="active" style="left:157px">Home</a>
  <a href="#" style="left:257px">About us</a>
  <a href="#" style="left:377px">Our Services</a>
  <div class="nav-mark">Kestwick<br>Holdings AG</div>
  <a href="#" style="left:716px">Our Blog</a>
  <a href="#" style="left:831px">Testmonial</a>
  <a href="#" class="btn-gold">Contact Us</a>
</header>

<section class="hero">
  <div class="hero-art" role="img" aria-label="Dark gold financial chart backdrop with a rising gold arrow sweeping across"></div>
  <div class="hero-name">Kestwick Holdings<small>AG</small></div>
  <h1 class="hero-title">We offer our customers<br>financial services</h1>
</section>

<section class="about">
  <div class="about-mark">Kestwick<br>Holdings AG</div>
  <div class="about-body">
    <p class="eyebrow">About us</p>
    <h2>Kestwick Holdings AG</h2>
    <p>Lorem ipsum dolor sit amet, consectetur adipiscing elit, sed do eiusmod tempor incididunt ut labore et dolore magna aliqua. Quis ipsum suspendisse ultrices gravida. Risus commodo viverra maecenas accumsan lacus vel facilisis. Lorem ipsum dolor sit amet, consectetur adipiscing elit, sed do eiusmod tempor incididunt ut labore et dolore magna aliqua.</p>
    <a href="#" class="btn-gold">Learn More</a>
  </div>
</section>

<section class="services">
  <p class="eyebrow">How it Work</p>
  <h2 class="section-title">Our Services</h2>
  <div class="service-list">
    <article class="service-card">
      <svg width="84" height="76" viewBox="0 0 84 76" fill="none" stroke="#b08b4a" stroke-width="3">
        <rect x="6" y="14" width="26" height="58"/><rect x="32" y="4" width="24" height="68"/><rect x="56" y="34" width="18" height="38"/>
        <path d="M12 24h14M12 34h14M12 44h14M12 54h14M38 14h12M38 24h12M38 34h12M38 44h12M38 54h12M0 72h84"/>
        <circle cx="78" cy="50" r="5"/>
      </svg>
      <h3>Real Estate</h3>
      <p>Lorem ipsum dolor sit amet, consectetur adipiscing elit, sed do eiusmod tempor incididunt ut labore et dolore magna aliqua.</p>
      <a href="#" class="circle-btn" aria-label="Real estate details"></a>
    </article>
    <article class="service-card">
      <svg width="84" height="76" viewBox="0 0 84 76" fill="none" stroke="#b08b4a" stroke-width="3">
        <circle cx="30" cy="22" r="18"/><path d="M44 34 L60 40"/><rect x="60" y="36" width="20" height="8" rx="3"/>
        <path d="M8 74 V58 C8 48 18 44 30 44 C42 44 50 48 50 58 V74 M54 74V62M64 74V54M74 74V48M0 74h84"/>
      </svg>
      <h3>Consumer Finance</h3>
      <p>Lorem ipsum dolor sit amet, consectetur adipiscing elit, sed do eiusmod tempor incididunt ut labore et dolore magna aliqua.</p>
      <a href="#" class="circle-btn" aria-label="Consumer finance details"></a>
    </article>
    <article class="service-card">
      <svg width="84" height="76" viewBox="0 0 84 76" fill="none" stroke="#b08b4a" stroke-width="3">
        <path d="M6 26 L42 4 L78 26 Z"/><rect x="10" y="26" width="64" height="8"/>
        <path d="M18 34v28M30 34v28M42 34v28M54 34v28M66 34v28"/><rect x="6" y="62" width="72" height="6"/><rect x="2" y="68" width="80" height="6"/>
        <text x="42" y="23" font-family="Cinzel,serif" font-size="9" fill="#b08b4a" stroke="none" text-anchor="middle">BANK</text>
      </svg>
      <h3>Banking</h3>
      <p>Lorem ipsum dolor sit amet, consectetur adipiscing elit, sed do eiusmod tempor incididunt ut labore et dolore magna aliqua.</p>
      <a href="#" class="circle-btn" aria-label="Banking details"></a>
    </article>
  </div>
</section>

<section class="testimonials">
  <p class="eyebrow">Client Reviews</p>
  <h2 class="section-title">Client Testimonial</h2>
  <div class="review-list">
    <article class="review">
      <svg width="34" height="26" viewBox="0 0 34 26" fill="#b08b4a"><path d="M0 26V13C0 5 4 1 12 0v5C8 6 7 8 7 11h7v15zM19 26V13C19 5 23 1 31 0v5c-4 1-5 3-5 6h7v15z"/></svg>
      <h3>Lorem ipsum dolor<br>sit amet, consectetur</h3>
      <p>Lorem ipsum dolor sit amet, consectetur adipiscing elit, sed do eiusmod tempor incididunt ut labore et dolore magna aliqua.</p>
      <div class="reviewer"><div class="avatar" role="img" aria-label="Client portrait"></div><div><b>Maren Holloway</b><span>Lorem Ipsum</span></div></div>
    </article>
    <article class="review">
      <svg width="34" height="26" viewBox="0 0 34 26" fill="#b08b4a"><path d="M0 26V13C0 5 4 1 12 0v5C8 6 7 8 7 11h7v15zM19 26V13C19 5 23 1 31 0v5c-4 1-5 3-5 6h7v15z"/></svg>
      <h3>Lorem ipsum dolor<br>sit amet, consectetur</h3>
      <p>Lorem ipsum dolor sit amet, consectetur adipiscing elit, sed do eiusmod tempor incididunt ut labore et dolore magna aliqua.</p>
      <div class="reviewer"><div class="avatar" role="img" aria-label="Client portrait"></div><div><b>Maren Holloway</b><span>Lorem Ipsum</span></div></div>
    </article>
  </div>
</section>

<section class="blog">
  <p class="eyebrow">Our Blog</p>
  <h2 class="section-title">Latest News</h2>
  <div class="post-grid">
    <article class="post">
      <div class="post-photo" role="img" aria-label="Hands typing on a laptop with security icons" style="background:linear-gradient(135deg,#6d5a4b,#c9c2bb 55%,#4a3d33)"></div>
      <div class="post-body"><h3>Lorem Ipsum</h3><time>March 09, 2022</time><p>Lorem ipsum dolor sit amet, consectetur adipiscing elit, sed do eiusmod tempor</p><a href="#">Learn More</a></div>
    </article>
    <article class="post">
      <div class="post-photo" role="img" aria-label="Person writing in a notebook at a desk" style="background:linear-gradient(135deg,#3a3633,#9d9690 50%,#2c2926)"></div>
      <div class="post-body"><h3>Lorem Ipsum</h3><time>March 09, 2022</time><p>Lorem ipsum dolor sit amet, consectetur adipiscing elit, sed do eiusmod tempor</p><a href="#">Learn More</a></div>
    </article>
    <article class="post">
      <div class="post-photo" role="img" aria-label="Business team meeting around a wooden table" style="background:linear-gradient(135deg,#4b3a2c,#a0764a 55%,#2a211a)"></div>
      <div class="post-body"><h3>Lorem Ipsum</h3><time>March 09, 2022</time><p>Lorem ipsum dolor sit amet, consectetur adipiscing elit, sed do eiusmod tempor</p><a href="#">Learn More</a></div>
    </article>
    <article class="post">
      <div class="post-photo" role="img" aria-label="Rising blue growth chart graphic" style="background:linear-gradient(135deg,#0b1a4a,#2f6bd6 55%,#0a1436)"></div>
      <div class="post-body"><h3>Lorem Ipsum</h3><time>March 09, 2022</time><p>Lorem ipsum dolor sit amet, consectetur adipiscing elit, sed do eiusmod tempor</p><a href="#">Learn More</a></div>
    </article>
  </div>
</section>

<section class="contact">
  <h2>Contact Us</h2>
  <ul class="contact-list">
    <li><svg width="12" height="16" viewBox="0 0 12 16" fill="#b08b4a"><path d="M6 0a6 6 0 0 0-6 6c0 4 6 10 6 10s6-6 6-10a6 6 0 0 0-6-6zm0 8.5A2.5 2.5 0 1 1 6 3.5a2.5 2.5 0 0 1 0 5z"/></svg><b>Address</b>Lorem ipsum dolor sit amet, consectetur adipiscing elit</li>
    <li><svg width="14" height="14" viewBox="0 0 14 14" fill="#b08b4a"><path d="M3 0l3 3-2 2c1 2 3 4 5 5l2-2 3 3-2 3C6 14 0 8 0 2z"/></svg><b>Phone</b>+1 555 010 0188</li>
    <li><svg width="15" height="12" viewBox="0 0 15 12" fill="#b08b4a"><path d="M0 0h15v2L7.5 7 0 2zM0 4l7.5 5L15 4v8H0z"/></svg><b>Email</b>info@kestwickholdings.com</li>
  </ul>
  <form class="contact-form">
    <div class="field">Name</div>
    <div class="field">Phone</div>
    <div class="field">Email</div>
    <div class="field">Messages</div>
    <a href="#" class="btn-gold">Submit</a>
  </form>
</section>

<footer class="site-footer">
  <div class="footer-art" role="img" aria-label="Soft gold glow where a sweeping gold arrow crosses the footer"></div>
  <div class="footer-name">Kestwick<br>Holdings AG</div>
  <div class="footer-col" style="left:423px">
    <h4>Quick Link</h4>
    <ul>
      <li><span class="chev"></span>Home</li><li><span class="chev"></span>About Us</li><li><span class="chev"></span>Our Services</li>
      <li><span class="chev"></span>Our Blog</li><li><span class="chev"></span>Testmonial</li><li><span class="chev"></span>Contact Us</li>
    </ul>
  </div>
  <div class="footer-col" style="left:622px">
    <h4>Follow Us</h4>
    <ul>
      <li><span class="dot"></span>Friendwall</li><li><span class="dot"></span>Snapgrid</li><li><span class="dot"></span>Chirper</li><li><span class="dot"></span>Viewtube</li>
    </ul>
  </div>
  <div class="footer-col" style="left:812px">
    <h4>Newsletter Updates</h4>
    <div class="news-field">Name*</div>
    <div class="news-field">Email*</div>
    <a href="#" class="btn-gold">Submit Now</a>
  </div>
  <p class="copyright">©Copyrights 2022 &nbsp;Kestwick Holdings &nbsp;&nbsp;All Rights Reserved</p>
</footer>

</body>
</html>
```